I need a business card design for a new company that will be doing consulting work around issues of cultural competency, and diversity and inclusion. I would like the design to be crisp and clear with bold but conservative colors and incorporate shades of blue

Target Market(s)

Small businesses, schools, non-profits

Industry/Entity Type

Consulting

Font styles to use
Serif
Sans Serif

Colors
0c5ba6
6b449b
3276b5
0292cd

Requirements
Must have
• A Morrow Venture (name of company)
• Lemlem Tavish
• CEO
• lemlem@amorrowventure.com
• (215)483-2756

```html
<!DOCTYPE html>
<html lang="en">
<head>
<meta charset="UTF-8">
<title>Lemlem Tavish — A Morrow Venture</title>
<link rel="stylesheet" href="https://fonts.googleapis.com/css2?family=Open+Sans:wght@700&display=swap">
<style>
  :root {
    --card-blue: #0c5ba6;
    --card-blue-light: #1c6fbd;
    --card-blue-deep: #0a5098;
    --mesh-glow: rgba(140, 195, 245, 0.30);
    --mesh-soft: rgba(140, 195, 245, 0.12);
    --ink-white: #ffffff;
  }
  html, body {
    margin: 0;
    padding: 0;
    width: 686px;
    height: 1200px;
    overflow: hidden;
  }
  .card {
    position: relative;
    width: 686px;
    height: 1200px;
    overflow: hidden;
    background: linear-gradient(165deg, var(--card-blue-light) 0%, var(--card-blue) 40%, var(--card-blue-deep) 100%);
    font-family: "Open Sans", "Segoe UI", Arial, sans-serif;
    color: var(--ink-white);
  }
  .mesh-accent {
    position: absolute;
    pointer-events: none;
  }
  .mesh-accent--left {
    left: -160px;
    top: 100px;
    width: 620px;
    height: 920px;
    background:
      radial-gradient(ellipse 40% 18% at 22% 46%, var(--mesh-glow) 0%, transparent 100%),
      radial-gradient(ellipse 70% 50% at 20% 45%, var(--mesh-soft) 0%, rgba(140, 195, 245, 0.05) 55%, transparent 80%);
  }
  .mesh-accent--right {
    right: -140px;
    bottom: -140px;
    width: 560px;
    height: 700px;
    background:
      radial-gradient(ellipse 45% 35% at 62% 62%, rgba(140, 195, 245, 0.20) 0%, transparent 100%),
      radial-gradient(ellipse 75% 60% at 60% 60%, var(--mesh-soft) 0%, transparent 80%);
  }
  .identity {
    position: absolute;
    left: 0;
    right: 0;
    top: 478px;
    display: flex;
    flex-direction: column;
    align-items: center;
    text-align: center;
  }
  .identity__icon {
    width: 100px;
    height: 90px;
    margin-bottom: 14px;
  }
  .identity__name {
    margin: 0;
    font-size: 68px;
    font-weight: 700;
    line-height: 1.1;
    letter-spacing: 0.5px;
  }
  .identity__company {
    margin: 14px 0 0;
    font-size: 31px;
    font-weight: 700;
    line-height: 1.2;
  }
</style>
</head>
<body>
  <main class="card">
    <div class="mesh-accent mesh-accent--left" role="img" aria-label="Fine-line mesh wave fanning in from the left edge"></div>
    <div class="mesh-accent mesh-accent--right" role="img" aria-label="Fine-line mesh wave in the lower right corner"></div>

    <section class="identity">
      <svg class="identity__icon" viewBox="0 0 100 90" aria-hidden="true">
        <circle cx="50" cy="22" r="22" fill="#ffffff"/>
        <path d="M2 90 C2 66 22 50 50 50 C78 50 98 66 98 90 Z" fill="#ffffff"/>
      </svg>
      <h1 class="identity__name">Lemlem Tavish</h1>
      <p class="identity__company">A Morrow Venture</p>
    </section>
  </main>
</body>
</html>
```